Independent theatre company and venue needs funky web design

Web design for theatre company based in Brisbane Australia. Innovative, grassroots theatre space needs to promote shows in quirky industrial venue. Design needs to be funky, arty but website feels solid and business savvy as well. We need a portal for selling tickets online.
Lamp and Ladder is the production company behind this project. We also create theatre in fresh, intimate and humanistic ways.
Target Market(s)
ages 20s-80s
Interested in the arts and fresh, quirky local experiences
Requirements
Must have
- Pages:
- Performances (What's on)
- Hire the Venue (info and enquiry form)
- About Lamp and Ladder (history and profile)
- Buy Tickets (patrons can purchase tickets to the shows on at the venue)
- Contact Us/Subscribe
Nice to have
- http://www.brickyard27stage.com/
- Similar in content to this one
- Ideally a website I can update shows (so wordpress or similar user friendly)

```html
<!DOCTYPE html>
<html lang="en">
<head>
<meta charset="utf-8">
<title>Lamp and Ladder – Performances</title>
<link href="https://fonts.googleapis.com/css2?family=Lobster&family=Open+Sans:wght@400;600&display=swap" rel="stylesheet">
<style>
:root{
  --ink:#000;
  --white:#fff;
  --paper:#ececec;
  --card:#ebebeb;
  --text:#444;
  --rule:#cfcfcf;
  --field:#2a2a2a;
  --wall:#8a2030;
  --wall-dark:#4a0c16;
}
*{margin:0;padding:0;box-sizing:border-box}
html,body{width:970px;height:1200px;overflow:hidden;background:var(--white)}
body{position:relative;font-family:"Open Sans",Arial,sans-serif;color:var(--text)}

.hero{position:absolute;left:0;top:0;width:970px;height:485px;overflow:hidden;background:#1a0406}
.hero-photo{position:absolute;inset:0;background:
  radial-gradient(ellipse 70px 150px at 130px 300px,rgba(228,80,80,.55),rgba(228,80,80,0) 100%),
  radial-gradient(ellipse 60px 140px at 330px 300px,rgba(220,70,70,.5),rgba(220,70,70,0) 100%),
  radial-gradient(ellipse 80px 170px at 470px 280px,rgba(200,110,90,.45),rgba(200,110,90,0) 100%),
  radial-gradient(ellipse 60px 140px at 640px 310px,rgba(225,70,70,.5),rgba(225,70,70,0) 100%),
  radial-gradient(ellipse 80px 170px at 830px 270px,rgba(205,115,95,.45),rgba(205,115,95,0) 100%),
  radial-gradient(ellipse 45px 10px at 480px 432px,rgba(0,0,0,.55),rgba(0,0,0,0)),
  linear-gradient(180deg,rgba(0,0,0,0) 0%,rgba(0,0,0,0) 84%,rgba(20,4,6,.85) 92%,#0e0304 100%),
  linear-gradient(90deg,rgba(0,0,0,.75) 0%,rgba(0,0,0,0) 10%,rgba(0,0,0,0) 88%,rgba(0,0,0,.35) 100%),
  radial-gradient(ellipse at 52% 30%,#a0283a 0%,var(--wall) 35%,#661421 70%,var(--wall-dark) 100%)}
.topbar{position:absolute;left:0;top:0;width:970px;height:38px;background:rgba(18,7,8,.85)}
.brand{position:absolute;left:0;top:0;width:294px;height:111px}
.brand-name{position:absolute;left:0;top:20px;width:294px;text-align:center;font-family:"Lobster",cursive;font-size:25px;line-height:28px;color:var(--ink);white-space:nowrap}
.nav{position:absolute;right:131px;top:12px;display:flex;gap:12px;font-size:10px;color:var(--white)}
.nav a{color:var(--white);text-decoration:none}
.nav a.current{text-decoration:underline}
.nav span{color:#bbb}
.caption{position:absolute;left:0;top:433px;width:970px;height:52px;background:linear-gradient(rgba(0,0,0,.5),rgba(0,0,0,.7));text-align:center;color:var(--white);font-family:"Lobster",cursive;font-size:31px;line-height:52px}

.shows{position:absolute;left:34px;top:534px;display:flex;gap:26.5px}
.show{width:160px;background:var(--card)}
.show-photo{height:108px}
.show-title{height:50px;display:flex;align-items:center;justify-content:center;text-align:center;font-family:"Lobster",cursive;font-size:14px;line-height:17px;color:#333;padding:0 14px;border-bottom:1px solid var(--rule)}
.show-date{height:22px;line-height:22px;text-align:center;font-size:8.5px;color:#555}

.actions{position:absolute;left:364px;top:750px;display:flex;gap:11px}
.btn{width:115px;height:26px;line-height:26px;background:var(--ink);color:var(--white);text-align:center;font-size:8.5px;text-decoration:none}

.welcome{position:absolute;left:0;top:826px;width:970px;height:189px;background:var(--paper);overflow:hidden}
.masks{position:absolute;left:750px;top:0;width:220px;height:189px;background:
  radial-gradient(ellipse 60px 70px at 55px 55px,#d8d8d8 60%,rgba(216,216,216,0) 100%),
  radial-gradient(ellipse 65px 75px at 130px 120px,#d6d6d6 60%,rgba(214,214,214,0) 100%)}
.welcome h2{position:absolute;left:0;top:34px;width:970px;text-align:center;font-family:"Lobster",cursive;font-weight:400;font-size:22px;color:#333}
.welcome .rule{position:absolute;top:47px;width:84px;height:1px;background:var(--rule)}
.welcome p{position:absolute;left:225px;top:78px;width:520px;text-align:center;font-size:10px;line-height:13.3px;color:#555}
.welcome a{position:absolute;left:0;top:136px;width:970px;text-align:center;font-size:9px;font-weight:600;color:#222}

.footer{position:absolute;left:0;top:1015px;width:970px;height:185px;background:var(--ink);color:var(--white)}
.footer h3{font-family:"Lobster",cursive;font-weight:400;font-size:16px;position:absolute;top:30px}
.addr{position:absolute;left:132px;top:57px;font-size:10px;line-height:12px}
.hours{position:absolute;left:132px;top:96px;font-size:8.5px;line-height:11px;color:#ccc}
.divider{position:absolute;top:33px;width:1px;height:92px;background:#222}
.social{position:absolute;left:384px;top:61px;display:flex;gap:9px}
.social span{width:11px;height:11px;border-radius:50%;background:var(--white)}
.field{position:absolute;top:60px;width:142px;height:27px;background:var(--field);border:1px solid #555;font-size:8px;color:#ccc;padding:0 7px;line-height:25px}
.signup{position:absolute;left:541px;top:102px;width:64px;height:24px;line-height:24px;background:var(--white);color:var(--ink);font-size:10px;text-align:center}
.baseline{position:absolute;left:131px;top:154px;width:708px;height:1px;background:#1e1e1e}
.legal{position:absolute;left:0;top:166px;width:970px;text-align:center;font-size:7.6px;color:#888}
.legal a{color:#aaa;margin-left:14px}
.legal .sep{margin-left:14px}
</style>
</head>
<body>

<header class="hero">
  <div class="hero-photo" role="img" aria-label="Dancers in red costumes leaping across a red-lit stage"></div>
  <div class="topbar"></div>
  <svg class="brand" viewBox="0 0 294 111" aria-hidden="true"><polygon points="0,0 294,0 147,111" fill="#fff"/></svg>
  <div class="brand-name">Lamp and Ladder</div>
  <nav class="nav">
    <a class="current" href="#">PERFORMANCES</a><span>-</span>
    <a href="#">HIRE THE VENUE</a><span>-</span>
    <a href="#">ABOUT LAMP AND LADDER</a><span>-</span>
    <a href="#">BUY TICKETS</a><span>-</span>
    <a href="#">CONTACT US</a>
  </nav>
  <div class="caption">Transforming Is Just The Beginning</div>
</header>

<section class="shows">
  <article class="show">
    <div class="show-photo" role="img" aria-label="Actor kneeling on a red industrial stage set" style="background:radial-gradient(ellipse 40px 45px at 95px 70px,rgba(30,10,8,.8),rgba(30,10,8,0)),linear-gradient(90deg,rgba(0,0,0,.3),rgba(0,0,0,0) 30%,rgba(0,0,0,0) 70%,rgba(0,0,0,.3)),linear-gradient(180deg,#b0382c 0%,#7a2018 45%,#2a0c08 100%)"></div>
    <div class="show-title">Lorem Ipsum is simply dummy text</div>
    <div class="show-date">8 FEB - 25 FEB</div>
  </article>
  <article class="show">
    <div class="show-photo" role="img" aria-label="Seated performer in warm golden light" style="background:radial-gradient(ellipse 55px 60px at 70px 50px,#b89a70,rgba(120,90,50,.5) 60%,rgba(0,0,0,0)),linear-gradient(90deg,#4a3c18,#2c2410 55%,#080604)"></div>
    <div class="show-title">Lorem Ipsum is simply dummy text</div>
    <div class="show-date">8 FEB - 25 FEB</div>
  </article>
  <article class="show">
    <div class="show-photo" role="img" aria-label="Two dancers in colourful costumes on a blue-lit stage" style="background:radial-gradient(ellipse 22px 40px at 62px 55px,rgba(150,80,200,.9),rgba(150,80,200,0)),radial-gradient(ellipse 30px 42px at 100px 62px,rgba(230,70,60,.9),rgba(230,70,60,0)),radial-gradient(ellipse 20px 14px at 105px 92px,rgba(240,180,40,.9),rgba(240,180,40,0)),linear-gradient(180deg,#0a1060,#1a2ab0 70%,#061040)"></div>
    <div class="show-title">Lorem Ipsum is simply dummy text</div>
    <div class="show-date">8 FEB - 25 FEB</div>
  </article>
  <article class="show">
    <div class="show-photo" role="img" aria-label="Actor reclining on a white chair on stage" style="background:radial-gradient(ellipse 55px 22px at 70px 70px,rgba(235,230,225,.9),rgba(235,230,225,0)),radial-gradient(ellipse 35px 16px at 120px 70px,rgba(140,50,40,.8),rgba(140,50,40,0)),linear-gradient(180deg,#2e2622 0%,#4a3c36 35%,#8a7268 70%,#a89a90 100%)"></div>
    <div class="show-title">Lorem Ipsum is simply dummy text</div>
    <div class="show-date">8 FEB - 25 FEB</div>
  </article>
  <article class="show">
    <div class="show-photo" role="img" aria-label="Performer in white stage makeup" style="background:radial-gradient(circle 75px at 95px 65px,#ece4e0 0%,#d8ccc8 55%,#9a8a88 80%,rgba(40,30,30,0) 100%),linear-gradient(135deg,#3a2e2e,#1a1414)"></div>
    <div class="show-title">Lorem Ipsum is simply dummy text</div>
    <div class="show-date">8 FEB - 25 FEB</div>
  </article>
</section>

<div class="actions">
  <a class="btn" href="#">ALL PERFORMANCES</a>
  <a class="btn" href="#">BUY TICKETS</a>
</div>

<section class="welcome">
  <div class="masks" role="img" aria-label="Faint comedy and tragedy masks decoration"></div>
  <span class="rule" style="left:318px"></span>
  <span class="rule" style="left:567px"></span>
  <h2>Welcome</h2>
  <p>Lorem ipsum dolor sit amet, consectetur adipiscing elit, sed do eiusmod tempor incididunt ut labore et dolore magna aliqua. Ut enim ad minim veniam, quis nostrud exercitation ullamco laboris nisi ut aliquip ex ea commodo consequat. Duis aute irure dolor in reprehenderit in voluptate velit esse cillum dolore eu fugiat nulla pariatur.</p>
  <a href="#">Read More</a>
</section>

<footer class="footer">
  <h3 style="left:131px">Lamp and Ladder</h3>
  <div class="addr">18 Kelvin Lane<br>Paddington QLD 4064</div>
  <div class="hours">Open during show seasons only :<br>Tuesday – Saturday 8pm</div>
  <span class="divider" style="left:328px"></span>
  <h3 style="left:377px">Find Us On</h3>
  <div class="social"><span></span><span></span><span></span></div>
  <span class="divider" style="left:492px"></span>
  <h3 style="left:541px">Signup For Newsletter</h3>
  <div class="field" style="left:541px">Name ...</div>
  <div class="field" style="left:697px">Email ...</div>
  <div class="signup">SIGNUP</div>
  <div class="baseline"></div>
  <div class="legal">COPYRIGHT © LAMP AND LADDER 2015-2016. ALL RIGHT RESERVED.<span class="sep">|</span><a href="#">TERMS &amp; CONDITIONS</a></div>
</footer>

</body>
</html>
```